Redesign of an existing homepage

This site needs a redesign
https://www.ferien-am-haldbach.de
This page with the accommodation options is important for the customer
https://www.ferien-am-haldbach.de/gastgeber/
Till now there is a new logo. See attachment. That's all I have.
It would make sense to use the colors of the logo in the redesign.
footer.jpg.
I would put this info into the footer. The graphic (Infomaterial) is not needed.
a new menu - links.jpg
This info can be put in a new menu. Therefore the right column is gone and there is more space for the design.
NEW:
Please keep in mind that the Icons are important and shall be displayed under every accommodation
Number of Pages Required
1 page

```html
<!DOCTYPE html>
<html lang="de">
<head>
<meta charset="utf-8">
<title>Tourismusverband Haldbach – Urlaub im Haldtal</title>
<link rel="stylesheet" href="https://fonts.googleapis.com/css2?family=Montserrat:wght@500;600;700&family=Questrial&display=swap">
<style>
:root{
  --blue:#27a2dc;
  --blue-dark:#1f7fb0;
  --ink:#1c1c1c;
  --paper:#faf8f7;
  --night:#100707;
  --nav-grey:#dcdcdc;
  --white:#ffffff;
}
*{box-sizing:border-box;margin:0;padding:0}
html,body{width:1200px;height:2438px;overflow:hidden}
body{position:relative;background:var(--paper);font-family:"Questrial",sans-serif;color:var(--ink)}
.brand{position:absolute;left:100px;top:14px;width:270px;display:flex;flex-direction:column;align-items:center;gap:14px}
.brand-mark{width:100px;height:100px;border-radius:50%;background:var(--blue)}
.brand-name{font-family:"Montserrat",sans-serif;font-weight:700;font-size:24px;line-height:1.1;color:var(--blue-dark);text-align:center}
.util-links{position:absolute;top:145px;left:619px;display:flex;gap:24px}
.util-links a{display:block;width:162px;height:35px;background:var(--blue);color:var(--white);text-decoration:none;font-size:26px;line-height:35px;text-align:center}
.main-nav{position:absolute;top:200px;left:0;width:1200px;height:52px;background:var(--nav-grey);box-shadow:0 4px 6px rgba(0,0,0,.12)}
.main-nav a{position:absolute;top:0;height:52px;line-height:52px;font-family:"Montserrat",sans-serif;font-weight:700;font-size:22px;color:var(--blue);text-decoration:none;white-space:nowrap}
.main-nav a.active{background:var(--blue);color:var(--white);left:0;width:129px;text-align:center}
.hero{position:absolute;top:252px;left:0;width:1200px;height:673px;background:linear-gradient(180deg,#d9d2c6 0%,#8a7d48 28%,#5f6a36 55%,#b47a3c 82%,#c49561 100%)}
.hero-tag{position:absolute;left:681px;top:582px;width:519px;height:170px;background:rgba(40,110,150,.72);color:var(--white);text-align:center;padding-top:42px}
.hero-tag h1{font-family:"Montserrat",sans-serif;font-weight:700;font-size:52px;line-height:1}
.hero-tag p{font-size:29px;margin-top:8px}
.wave{position:absolute;left:0;top:0}
.welcome{position:absolute;left:78px;top:968px;width:767px;font-size:21.5px;line-height:30.7px;text-align:justify;letter-spacing:.2px}
.welcome p+p{margin-top:30.7px}
.office-card{position:absolute;left:897px;top:927px;width:272px;height:440px;background:var(--night);color:var(--white);padding:95px 0 0 27px;font-family:"Montserrat",sans-serif;font-weight:600;font-size:14px;line-height:20.3px}
.office-card h2{font-size:44px;color:var(--blue);font-weight:600;line-height:1;margin:0 0 8px 0}
.office-card p+p{margin-top:20px}
.promo-photo{position:absolute;left:776px;top:1500px;width:424px;height:718px;background:linear-gradient(180deg,rgba(39,162,220,0) 0%,#c8553f 45%,#b52f2f 80%,#7d8fa8 100%);border-radius:200px 200px 0 0}
.partners{position:absolute;left:0;top:1774px;width:161px;height:444px;background:var(--white);padding:30px 12px;display:flex;flex-direction:column;gap:22px}
.partner-badge{width:127px;border-radius:3px}
.footer{position:absolute;left:0;top:2218px;width:1200px;height:220px;background:var(--night);color:var(--white);font-size:18px;line-height:24px}
.footer h3{font-family:"Montserrat",sans-serif;font-weight:600;font-size:23px;line-height:28px;color:var(--blue)}
.footer-col{position:absolute;top:22px}
.footer-col h3{margin-bottom:18px}
.footer .chip{display:inline-block;background:var(--blue);color:var(--white);text-decoration:none;padding:0 6px;height:27px;line-height:27px;font-size:18px}
</style>
</head>
<body>

<header>
  <div class="brand"><span class="brand-mark"></span><span class="brand-name">Tourismusverband<br>Haldbach</span></div>
  <nav class="util-links"><a href="#">Infomaterial</a><a href="#">Impressum</a><a href="#">Datenschutz</a></nav>
  <nav class="main-nav">
    <a class="active" href="#">HOME</a>
    <a href="#" style="left:137px">GASTGEBER</a>
    <a href="#" style="left:296px">HALDTAL</a>
    <a href="#" style="left:424px">FREIZEIT</a>
    <a href="#" style="left:551px">AUSFLUGSZIELE</a>
    <a href="#" style="left:776px">KUNST UND KULTUR</a>
    <a href="#" style="left:1051px">KONTAKT</a>
  </nav>
</header>

<section class="hero" role="img" aria-label="Foto einer Familie mit Kleinkind beim Spaziergang durch herbstliche Landschaft im Abendlicht"></section>
<div class="hero-tag"><h1>Urlaub im Haldtal</h1><p>dem schönsten Fleck Bayerns</p></div>

<svg class="wave" width="1200" height="2438" viewBox="0 0 1200 2438" aria-hidden="true">
  <path fill="#27a2dc" d="M1200 1300 C1060 1330 990 1400 980 1500 C970 1600 900 1660 840 1700 C720 1780 660 1880 560 1905 C470 1930 420 1890 340 1830 C240 1750 120 1720 0 1745 L0 2218 L1200 2218 Z"/>
</svg>

<main class="welcome">
  <p>Lieber Besucherinnen und Besucher,<br>Haldbach und Umgebung haben all das, was das Leben lebenswert macht:<br>Kultur und Natur, Lebensfreude und Genuss, freundliche und aufgeschlossene Menschen...</p>
  <p>Ob Kirchen, Brunnen oder andere Baudenkmäler - bei einem Rundgang durch die Haldtaler Ross-Stadt kann man viele liebevolle Details für sich entdecken.</p>
  <p>Für Bewegungsfreudige und Erholungssuchende gibt es "Natur pur" in und um Haldbach! Hier kann man sportlich unterwegs sein beim Radeln, Walken, Wandern, Golfen, Reiten und Baden oder einfach nur die Ruhe genießen.</p>
  <p>Freizeit und Erholung für die ganze Familie - planen Sie einen Urlaub auf dem Bauernhof, in einer Ferienwohnung oder im Hotel. Ihr Urlaub im Haldtal wird ein einmaliges Erlebnis!</p>
  <p>Genießen Sie unsere Gastfreundschaft - ein Besuch lohnt sich zu jeder Jahreszeit.<br>Wir freuen uns auf Sie!<br>Ihr</p>
  <p>Fremdenverkehrsverein Haldbach und Umgebung e. V.</p>
</main>

<aside class="office-card">
  <h2>FVV HAB</h2>
  <p>Fremdenverkehrsverein<br>Haldbach und Umgebung e. V.<br>Marktplatz 4<br>84999 Haldbach</p>
  <p>Tel.: 08999 / 204 7710<br>Fax: 08999 / 204 7719<br>tourist-info@haldbach.de</p>
  <p>Öffnungszeiten:<br>Mo-Fr 9:00 - 17:00 Uhr<br>Mai-Oktober:<br>Sa 9:00-12:00 Uhr</p>
</aside>

<div class="promo-photo" role="img" aria-label="Foto einer jungen Frau im rot-weiß gestreiften Shirt, die begeistert auf den Text zeigt"></div>

<div class="partners">
  <div class="partner-badge" style="height:88px;background:#2f74b8"></div>
  <div class="partner-badge" style="height:140px;background:#9fd0e6"></div>
  <div class="partner-badge" style="height:62px;background:#a9d6ef"></div>
  <div class="partner-badge" style="height:62px;background:#a9d6ef"></div>
</div>

<footer class="footer">
  <div class="footer-col" style="left:28px"><h3 style="margin-bottom:10px">Fremdenverkehrsverein<br>Haldbach und Umgebung e. v.</h3><p>Marktplatz 4<br>84999 Haldbach</p></div>
  <div class="footer-col" style="left:428px"><h3>Kontakt</h3><p>Tel.: 08999 / 204 7710<br>Fax: 08999 / 204 7719</p><a class="chip" href="#" style="margin-top:20px">-tourist-info@haldbach.de</a></div>
  <div class="footer-col" style="left:705px"><h3>Öffnungszeiten</h3><p>Mo-Do 9:00 - 16:00 Uhr<br>Fr&nbsp;&nbsp;&nbsp;&nbsp;&nbsp;&nbsp;&nbsp;&nbsp;&nbsp;&nbsp;9:00 - 12:30 Uhr</p></div>
  <div class="footer-col" style="left:970px"><h3>Quicklinks</h3><a class="chip" href="#" style="width:206px">Veranstaltungskalender</a><br><a class="chip" href="#" style="width:206px;margin-top:20px">Infomaterial</a></div>
</footer>

</body>
</html>
```